Web Design Project - Old Brackley (Bar)

We need a website for a new wine bar/hotel opening in Sydney's Kings Cross area. The concept is a rustic Australiana bar. We intend to use raw materials (sandstone, rusty metal etc) and lots of greenery/plants. It is set to be stylish and accessible to a young and middle age clientele.

The idea is to bring the outside inside.

The venue can cater for 450 people and is in one of the major nightclub strips in Australia. The demographic differs from celebrities to backpackers.

Target Market(s)

We are targeting 23yr - 40yr olds.

Industry/Entity Type

Hotel

Requirements
Must have
• What I want is a design to reflect is the fit out of the bar. We would like to see a rustic design to reflect the theme of the bar. The theme behind the fit out will be "bringing the outside inside" with lots of plants, wet walls etc.. There will be exposed brickwork, sandstone, timber and rusted steel with laser cut designs throughout the venue.
Nice to have
• I've attached some 3D designs that the venue will be roughly based on.

```html
<!DOCTYPE html>
<html lang="en">
<head>
<meta charset="utf-8">
<title>Old Brackley – About us</title>
<link rel="stylesheet" href="https://fonts.googleapis.com/css2?family=Merriweather:wght@400;700;900&family=Open+Sans:wght@400;600;700&display=swap">
<style>
  :root {
    --wood-dark: #2a170c;
    --wood: #4a2a16;
    --wood-mid: #6b4324;
    --sandstone: #8a6a46;
    --sandstone-light: #a88a63;
    --cream: #e9d3ac;
    --cream-light: #f3e4c7;
    --panel: #dcc096;
    --rust: #8b1a10;
    --maroon: #5e0d10;
    --ink: #2b1a10;
    --text: #4a3322;
    --nav-text: #f3e4c7;
    --gold: #e06a16;
  }
  * { box-sizing: border-box; margin: 0; padding: 0; }
  html, body { width: 781px; height: 1200px; overflow: hidden; }
  body {
    font-family: "Open Sans", sans-serif;
    color: var(--text);
    background: var(--wood-dark);
    position: relative;
  }
  .site-header {
    position: absolute; left: 0; top: 0; width: 781px; height: 229px;
    background: linear-gradient(180deg, var(--wood-mid) 0%, var(--sandstone) 40%, var(--sandstone-light) 70%, var(--sandstone) 100%);
  }
  .header-planks {
    position: absolute; left: 0; top: 0; width: 100%; height: 78px;
    background: repeating-linear-gradient(90deg, var(--wood) 0 62px, var(--wood-dark) 62px 64px);
    opacity: .85;
  }
  .brand {
    position: absolute; left: 0; top: 92px; width: 100%;
    text-align: center;
  }
  .brand-mark {
    display: inline-block; width: 74px; height: 74px;
    background: var(--ink);
    margin-bottom: 10px;
  }
  .brand-name {
    display: block;
    font-family: "Merriweather", serif; font-weight: 400;
    font-size: 24px; letter-spacing: 2px; color: var(--ink);
  }
  .main-nav {
    position: absolute; left: 0; top: 229px; width: 781px; height: 41px;
    background: linear-gradient(180deg, var(--wood) 0%, var(--wood-dark) 100%);
    display: flex; justify-content: space-around; align-items: center;
    padding: 0 40px;
  }
  .main-nav a {
    color: var(--nav-text); text-decoration: none;
    font-weight: 700; font-size: 13px; letter-spacing: .5px;
  }
  .content-panel {
    position: absolute; left: 13px; top: 270px; width: 755px; height: 672px;
    background: var(--panel);
    padding: 40px 18px 0;
  }
  .page-title {
    font-family: "Merriweather", serif; font-weight: 900;
    font-size: 44px; color: var(--rust); line-height: 1;
    margin-bottom: 12px;
  }
  .lead {
    font-family: "Merriweather", serif; font-weight: 700;
    font-size: 15px; line-height: 20px; color: var(--ink);
  }
  .venue-photo {
    position: absolute; left: 18px; top: 138px; width: 719px; height: 242px;
    background: linear-gradient(135deg, #3a2010 0%, #7a4a24 35%, #b08050 55%, #5a3418 80%, #2a1608 100%);
  }
  .column {
    position: absolute; top: 404px;
  }
  .column-left { left: 18px; width: 470px; }
  .column-right { left: 507px; width: 230px; }
  .subtitle {
    font-family: "Merriweather", serif; font-weight: 700;
    font-size: 16px; color: var(--rust); margin-bottom: 10px;
  }
  .body-text {
    font-size: 11px; line-height: 16px; color: var(--text);
    margin-bottom: 22px;
  }
  .reserve-button {
    display: block; width: 230px; height: 34px; margin-top: 6px;
    background: var(--maroon); color: var(--cream-light);
    font-family: "Merriweather", serif; font-weight: 700; font-size: 14px;
    text-align: center; line-height: 34px; text-decoration: none;
  }
  .info-band {
    position: absolute; left: 0; top: 942px; width: 781px; height: 182px;
    background: linear-gradient(180deg, var(--wood) 0%, var(--wood-dark) 100%);
  }
  .info-card {
    position: absolute; top: 26px; width: 224px; height: 130px;
    background: var(--cream-light);
    text-align: center; padding-top: 16px;
  }
  .info-card h2 {
    font-family: "Merriweather", serif; font-weight: 900;
    font-size: 22px; color: var(--ink); line-height: 1.1; margin-bottom: 6px;
  }
  .info-card p { font-size: 11px; line-height: 15px; color: var(--text); padding: 0 14px; }
  .info-card .hours {
    font-family: "Merriweather", serif; font-weight: 700;
    font-size: 16px; color: var(--rust); margin-top: 6px;
  }
  .directions-button {
    display: inline-block; margin-top: 10px; padding: 0 14px;
    height: 24px; line-height: 24px;
    background: var(--panel); color: var(--rust);
    font-size: 11px; font-weight: 700; text-decoration: none;
  }
  .card-where { left: 31px; }
  .card-hours { left: 278px; }
  .card-chef { left: 526px; }
  .site-footer {
    position: absolute; left: 0; top: 1124px; width: 781px; height: 76px;
    background: var(--wood-dark);
    display: flex; align-items: center; justify-content: space-between;
    padding: 0 22px;
    color: var(--cream);
    font-size: 11px;
  }
  .social { display: flex; gap: 10px; }
  .social span { width: 14px; height: 14px; border-radius: 50%; background: var(--cream); display: block; }
</style>
</head>
<body>
  <header class="site-header">
    <div class="header-planks"></div>
    <div class="brand">
      <span class="brand-mark"></span>
      <span class="brand-name">Old Brackley</span>
    </div>
  </header>

  <nav class="main-nav">
    <a href="#">HOME</a>
    <a href="#">ABOUT US</a>
    <a href="#">MENU</a>
    <a href="#">RESERVATIONS</a>
    <a href="#">LOCATION</a>
  </nav>

  <main class="content-panel">
    <h1 class="page-title">About us</h1>
    <p class="lead">I'm a paragraph. Click here to add your own text and edit me.<br>
    It's easy. Just click "Edit Text" or double click me and you can start adding your own content...</p>

    <div class="venue-photo" role="img" aria-label="Photo of the bar interior with brick walls, hanging lights and guests at tables"></div>

    <section class="column column-left">
      <h3 class="subtitle">I'm a subtitle.</h3>
      <p class="body-text">I'm a Paragraph. Click here to add your own text and edit me. It's easy. Just click "Edit Text" or double click me and you can start adding your own content and make changes to the font. Feel free to drag and drop me anywhere you like on your page. I'm a great place for you to write more...</p>
      <h3 class="subtitle">I'm a subtitle.</h3>
      <p class="body-text">I'm a Paragraph. Click here to add your own text and edit me. It's easy. Just click "Edit Text" or double click me and you can start adding your own content and make changes to the font. Feel free to drag and drop me anywhere you like on your page. I'm a great place for you to write more...</p>
    </section>

    <section class="column column-right">
      <h3 class="subtitle">I'm a subtitle.</h3>
      <p class="body-text">I'm a Paragraph. Click here to add your own text and edit me. It's easy. Just click "Edit Text" or double click me and you can start adding your own content and make changes to the font. Feel free to drag and drop me anywhere you like on your page...</p>
      <a class="reserve-button" href="#">Make a reservation</a>
    </section>
  </main>

  <section class="info-band">
    <div class="info-card card-where">
      <h2>WHERE ARE WE?</h2>
      <p>48 Larch Lane, Sydney, AU 2011</p>
      <a class="directions-button" href="#">GET DIRECTIONS NOW</a>
    </div>
    <div class="info-card card-hours">
      <h2>OPENING HOURS</h2>
      <p>We're open everyday</p>
      <p class="hours">12:00pm-1:00am</p>
    </div>
    <div class="info-card card-chef">
      <h2>CHEF AT HOME</h2>
      <p>I'm a Paragraph. Click here to add your own text and edit me. I'm a great place for you.</p>
    </div>
  </section>

  <footer class="site-footer">
    <span>© 2013 by Old Brackley.</span>
    <div class="social"><span></span><span></span><span></span></div>
  </footer>
</body>
</html>
```